Website for Sports and Exercise Medicine Doctor with active research in stem cells therapies.

I am a sports and exercise medicine doctor with research interests in the cutting edge areas of biological therapies, most notable stem cells. None of my patients are dying of anything, and most of them come to see me to decrease their pain, so they can get back to what they want to do.

The approach i then take is to decrease their pain and support them to achieve the things they wish to achieve. Most people start at "Just make it stop hurting doc" , but I try to move them towards something more important over time.

I would like the website to be very different to other "Doctor or medical websites" in its look. No pictures of doctors in white coats and no pictures of fit old people smiling. I would potentially like the fist thing seen to be a quote:

"Less pain. Everybody wants it, but what are you going to do, once you've got it?"

(But this is only an idea, I am open to anything)

The website will need a couple of things

1. "Locations" I work
2. "Research" I am involved in
3. "Sort Me out" - Clinical information for people to access
4. "Social" - imbedded chirpline and friendgrid
5. "Blog" - imbedded postmill blog
6. "Bio" - the usual bio-stuff

The "Sort Me out" - pages I would like to have the functionality as seen in this site http://www.vandrolix.com.au/platelet/. I intend to put disease topics into these pages (eg Achilles tehdinopathy, osteoarthritis etc etc etc). Once again I am not wedded to this but something along these lines would be good.

To give you an idea these are some sites I like
http://www.harborlantern.com/
http://quimbet.com/
http://orvanstudio.com.sg/
http://milbonhonestkettle.com/
http://www.tessmonthly.com/
http://gravwick.com/#offering
http://pelicanworks.tv/
http://tidalnova.com/
http://foxledger.co.uk/#about

Target Market(s)

20-80 year old.
People with tendon injuries
People with osteoarthritis
People interested in stem cells
I will build the site over time to contain information on multiple sporting injuries and musculoskeletal disorders. It will also become a site for the latest on stem cell research particularly in the area of osteoarthritis.

Industry/Entity Type

Medical

Font styles to use
Sans Serif

Colors
ffffff

Requirements
Nice to have
• To give you an idea these are some sites I like
http://quimbet.com/
http://pelicanworks.tv/
http://tidalnova.com/
Should not have
• Pictures of doctors in white coats or old fit people smiling

```html
<!DOCTYPE html>
<html lang="en">
<head>
<meta charset="utf-8">
<title>Sort Me Out – Dr Kel Varden</title>
<link href="https://fonts.googleapis.com/css2?family=Lato:wght@300;400;700&display=swap" rel="stylesheet">
<style>
:root{
  --teal:#34778b;
  --teal-bright:#2aa3c0;
  --ink:#333;
  --body:#555;
  --muted:#777;
  --panel:#f2f2f2;
  --footer:#3e3d44;
  --white:#fff;
}
*{margin:0;padding:0;box-sizing:border-box}
html,body{width:971px;height:1200px;overflow:hidden;background:var(--white);font-family:"Lato",sans-serif;color:var(--body)}
.page{position:relative;width:971px;height:1200px}
.abs{position:absolute}

.logo{left:94px;top:26px;font-size:46px;font-weight:300;color:var(--teal);letter-spacing:1px;line-height:1}
.search{left:734px;top:16px;width:146px;height:21px;background:#5a5a5a;color:#eee;font-size:12px;line-height:21px;padding-left:8px}
.search-btn{position:absolute;right:0;top:0;width:20px;height:21px;background:var(--teal)}
.nav{top:63px;left:0;font-size:11px;letter-spacing:1.2px;color:var(--ink);font-weight:400}
.nav a{position:absolute;white-space:nowrap;text-decoration:none;color:inherit}
.nav-active{left:582px;top:97px;width:84px;height:4px;background:var(--teal)}

.hero{left:9px;top:103px;width:952px;height:89px;background:linear-gradient(90deg,#3a3c44 0%,#5b5f68 30%,#2b2f38 55%,#c9a890 70%,#8fb4d4 90%,#c5d8ea 100%)}

.crumb{left:88px;top:199px;font-size:9px;color:var(--muted)}
.title{left:88px;top:224px;font-size:27px;font-weight:700;color:var(--teal);letter-spacing:.3px}
.title-rule{left:89px;top:265px;width:522px;height:1px;background:#888}
.title-accent{left:89px;top:262px;width:73px;height:4px;background:var(--teal)}
.lead{left:89px;top:293px;font-size:19px;font-weight:400;color:var(--teal)}
.copy{width:522px;font-size:13px;line-height:17.4px;font-weight:300;color:var(--body)}

.acc{left:89px;width:521px;background:var(--panel);font-size:18px;color:var(--ink);padding-left:12px;font-weight:400}
.acc-open{top:488px;height:37px;line-height:36px;border-bottom:2px solid var(--teal)}
.acc-closed{height:38px;line-height:38px}
.acc svg{position:absolute;right:12px;top:9px}

.side-head{left:627px;width:253px;height:43px;background:var(--teal);color:var(--white);font-size:17px;font-weight:300;text-align:center;line-height:45px;letter-spacing:.5px}
.tweet{left:656px;top:289px;width:205px;font-size:12px;line-height:15px;color:var(--ink)}
.tweet span{color:var(--teal-bright)}
.tweet-time{left:656px;top:340px;font-size:8px;font-style:italic;color:var(--ink)}
.follow{left:681px;top:366px;font-size:12px;font-weight:700;color:var(--teal);text-decoration:underline;letter-spacing:.3px}
.blog-img{left:627px;top:457px;width:254px;height:105px;background:linear-gradient(90deg,#5ea6cf,#a9cfe6 55%,#dbe9f3)}
.blog-title{left:627px;top:576px;font-size:15px;font-weight:700;color:var(--teal)}
.blog-date{left:629px;top:600px;font-size:7px;font-style:italic;color:var(--ink)}
.blog-copy{left:629px;top:624px;width:250px;font-size:11px;line-height:14.2px;font-weight:300;color:var(--body)}

.quote-band{left:9px;top:830px;width:952px;height:208px;background:var(--panel)}
.quote-badge{left:451px;top:797px;width:66px;height:66px;border-radius:50%;background:var(--white)}
.quote-text{left:9px;top:896px;width:952px;text-align:center;font-size:18px;line-height:22px;font-weight:300;color:var(--ink)}
.quote-name{left:9px;top:961px;width:952px;text-align:center;font-size:13px;color:var(--teal)}
.dots{left:457px;top:991px;display:flex;gap:6px}
.dots i{width:9px;height:9px;border-radius:50%;background:#3e3d44;display:block}
.dots i:first-child{background:var(--teal)}

.footer{left:9px;top:1038px;width:952px;height:127px;background:var(--footer)}
.footer-logo{left:9px;top:1052px;width:952px;text-align:center;font-size:46px;font-weight:300;color:var(--white);line-height:1}
.social{top:1132px;width:23px;height:23px;background:#000}
.bar{left:9px;top:1165px;width:952px;height:26px;background:var(--teal);color:var(--white);font-size:9px;font-weight:700;line-height:26px}
.bar span{position:absolute}
</style>
</head>
<body>
<div class="page">
  <header>
    <div class="abs logo">drkv</div>
    <div class="abs search">Search Me
      <div class="search-btn"><svg width="20" height="21" viewBox="0 0 20 21"><circle cx="9.5" cy="9.5" r="3" fill="none" stroke="#fff" stroke-width="1.5"/><line x1="11.7" y1="11.7" x2="14" y2="14" stroke="#fff" stroke-width="1.6"/></svg></div>
    </div>
    <nav class="abs nav">
      <a style="left:267px">HOME</a>
      <a style="left:338px">FIND A GREAT CLINICIAN</a>
      <a style="left:501px">RESEARCH</a>
      <a style="left:587px">SORT ME OUT</a>
      <a style="left:695px">BIO</a>
      <a style="left:751px">LOCATION</a>
      <a style="left:830px">BLOG</a>
    </nav>
    <div class="abs nav-active"></div>
  </header>

  <div class="abs hero" role="img" aria-label="Banner photo of a boxer in gloves training"></div>

  <main>
    <div class="abs crumb">home / sort me out</div>
    <h1 class="abs title">SORT ME OUT</h1>
    <div class="abs title-rule"></div>
    <div class="abs title-accent"></div>
    <h2 class="abs lead">Integer eget accumsan lorem. Integer sodales</h2>
    <p class="abs copy" style="left:89px;top:331px">Duis et sem mauris. Donec est sapien, eleifend et sollicitudin ut, dapibus ut arcu. Cras id euismod sem, eget elementum nisl. Fusce quis nunc blandit, lobortis lacus sit amet, semper tortor. Sed viverra eros a lorem condimentum, eget pellentesque augue facilisis. Donec molestie fermentum diam fringilla lobortis. Vestibulum mollis ornare magna non faucibus. Quisque varius, ipsum eget tristique ornare, elit arcu porta risus, nec dignissim enim ligula semper velit. Proin dignissim velit ligula, at fringilla nunc dignissim sed. Ut id eros vitae odio ullamcorper pharetra sed ut nisi. Vivamus vel elit est.</p>

    <div class="abs acc acc-open">Vestibulum libero leo, accumsan in nisl.
      <svg width="20" height="20"><line x1="1" y1="10" x2="19" y2="10" stroke="#999" stroke-width="1"/></svg>
    </div>
    <p class="abs copy" style="left:89px;top:541px">Duis et sem mauris. Donec est sapien, eleifend et sollicitudin ut, dapibus ut arcu. Cras id euismod sem, eget elementum nisl. Fusce quis nunc blandit, lobortis lacus sit amet, semper tortor. Sed viverra eros a lorem condimentum, eget pellentesque augue facilisis. Donec molestie fermentum diam fringilla lobortis. Vestibulum mollis ornare magna non faucibus. Quisque varius, ipsum eget tristique ornare, elit arcu porta risus, nec dignissim enim ligula semper velit. Proin dignissim velit ligula, at fringilla nunc dignissim sed. Ut id eros vitae odio ullamcorper pharetra sed ut nisi. Vivamus vel elit est.</p>

    <div class="abs acc acc-closed" style="top:696px">Etiam consectetur dictum magna.
      <svg width="20" height="20"><line x1="1" y1="10" x2="19" y2="10" stroke="#999"/><line x1="10" y1="1" x2="10" y2="19" stroke="#999"/></svg>
    </div>
    <div class="abs acc acc-closed" style="top:741px">What happens after treatment?
      <svg width="20" height="20"><line x1="1" y1="10" x2="19" y2="10" stroke="#999"/><line x1="10" y1="1" x2="10" y2="19" stroke="#999"/></svg>
    </div>
  </main>

  <aside>
    <div class="abs side-head" style="top:222px">CHIRPLINE FEED</div>
    <p class="abs tweet">@Tomas_Rielly <span>Hi . Great to meet you outside of the forum</span></p>
    <div class="abs tweet-time">2 months ago</div>
    <div class="abs follow">FOLLOW US ON CHIRPLINE</div>

    <div class="abs side-head" style="top:414px">LATEST BLOG</div>
    <div class="abs blog-img" role="img" aria-label="Blog photo of two people exercising on gym machines"></div>
    <h3 class="abs blog-title">CRAS A TEMPOR LEO.</h3>
    <div class="abs blog-date">December 15, 2013</div>
    <p class="abs blog-copy">Pellentesque habitant morbi tristique senectus et netus et malesuada fames ac turpis egestas. Curabitur volutpat augue lectus, ut lacinia ante tempor quis. Etiam gravida pellentesque sem, et</p>
  </aside>

  <section>
    <div class="abs quote-band"></div>
    <div class="abs quote-badge">
      <svg width="66" height="66" viewBox="0 0 66 66"><g fill="#34778b"><circle cx="26" cy="35" r="6"/><path d="M21 35 Q21 25 29 22 L30 24 Q25 27 25 33 Z"/><circle cx="41" cy="35" r="6"/><path d="M36 35 Q36 25 44 22 L45 24 Q40 27 40 33 Z"/></g></svg>
    </div>
    <blockquote class="abs quote-text">“ Lorem ipsum dolor sit amet, consectetur adipiscing elit. In imperdiet diam augue,<br>vitae lacinia leo lacinia sit amet. Nulla facilisi. Cras cursus sed odio a mollis”</blockquote>
    <div class="abs quote-name">Dr Kel Varden</div>
    <div class="abs dots"><i></i><i></i><i></i><i></i></div>
  </section>

  <footer>
    <div class="abs footer"></div>
    <div class="abs footer-logo">drkv</div>
    <div class="abs social" style="left:410px" aria-label="friendgrid"></div>
    <div class="abs social" style="left:447px" aria-label="circlepost"></div>
    <div class="abs social" style="left:484px" aria-label="chirpline"></div>
    <div class="abs social" style="left:522px" aria-label="workweave"></div>
    <div class="abs bar">
      <span style="left:82px">Copyright 2013 - www.drkelvarden.com.au - All Rights Reserved</span>
      <span style="left:605px">Phone: +61 02 555-01-42</span>
      <span style="left:726px">E-mail: <u>hello@drkelvarden.com.au</u></span>
    </div>
  </footer>
</div>
</body>
</html>
```